Brightmere Foot Works patient advertisement flyer

We need a flyer for a new fungal nail treatment clinic called brightmere foot works. We require a flyer/brochure that advertises our clinic and what we do (please find attached a document that has the information we would like included - we are completely open to the designer structuring the information how they see fit so long as it encompasses the information provided). We also have a booklet that we give to patients on their initial consult (which I have attached to give you an idea of the colour schemes /design that we are already using and we would like our brochure to align with this booklet). I have also attached our logo for use in the brochure. Finally, I have attached a copy of our cold laser brochure and associated pictures - ideally we would like to capture something similar to this brochure and have a picture of the laser somewhere on the brochure. We would like our brochure to communicate professional but be sleek, modern and have a minimalist look.

Can we please make these tri fold outs please like a brochure format 😊

```html
<!DOCTYPE html>
<html lang="en">
<head>
<meta charset="utf-8">
<title>Brightmere Foot Works – Tri-fold Brochure</title>
<link href="https://fonts.googleapis.com/css2?family=Montserrat:wght@300;400&family=Libre+Baskerville:wght@700&family=Tinos&display=swap" rel="stylesheet">
<style>
  :root{
    --brand-blue:#4169b4;
    --pale-blue:#d3dff0;
    --ink:#1c1c1c;
    --white:#ffffff;
    --strip-grey:#dcdcdc;
  }
  *{margin:0;padding:0;box-sizing:border-box}
  html,body{width:1200px;height:848px;overflow:hidden;background:var(--white)}
  .brochure{position:relative;width:1200px;height:848px;overflow:hidden;background:var(--white);font-family:'Montserrat',sans-serif}

  /* inside-left panel */
  .panel-intro{position:absolute;left:0;top:0;width:400px;height:848px}
  .intro-backdrop{position:absolute;left:20px;top:0;width:355px;height:480px;background:var(--pale-blue);border-radius:0 0 178px 178px}
  .photo-ring{position:absolute;border-radius:50%;background:var(--white)}
  .photo{position:absolute;border-radius:50%}
  .intro-ring{left:32px;top:136px;width:332px;height:332px}
  .laser-photo{left:38px;top:142px;width:320px;height:320px;background:radial-gradient(circle at 45% 45%,#e0479d 0%,#c15a7a 35%,#b8a6a6 70%,#cfc8c8 100%)}
  .rule{position:absolute;height:3px;background:var(--brand-blue)}
  .intro-rule{left:110px;top:577px;width:187px}
  .intro-text{position:absolute;left:32px;top:598px;width:343px;font-size:14.4px;line-height:17.2px;color:var(--ink);text-align:justify;text-align-last:center;font-weight:400}

  /* centre contact panel */
  .panel-contact{position:absolute;left:400px;top:0;width:401px;height:848px;background:var(--brand-blue)}
  .feet-photo{position:absolute;left:0;top:0;width:401px;height:470px;background:linear-gradient(180deg,#3d5a8e 0%,#41609c 55%,#4169b4 100%)}
  .contact-name{position:absolute;left:0;top:508px;width:401px;text-align:center;font-family:'Montserrat',sans-serif;font-weight:400;font-size:20px;letter-spacing:1px;color:var(--white)}
  .contact-icons{position:absolute;left:101px;top:622px;width:200px;height:40px;display:flex;justify-content:space-between}
  .icon-badge{width:39px;height:39px;border-radius:50%;background:var(--white);display:flex;align-items:center;justify-content:center}
  .icon-badge svg{width:22px;height:22px}
  .contact-line{position:absolute;left:0;width:401px;text-align:center;font-weight:300;font-size:14.6px;color:var(--white);letter-spacing:.3px}

  /* front cover panel */
  .panel-cover{position:absolute;left:801px;top:0;width:399px;height:848px;background:linear-gradient(90deg,var(--strip-grey) 0px,#f4f4f4 60px,var(--white) 80px)}
  .cover-mark{position:absolute;left:155px;top:32px;width:90px;height:90px;border-radius:50%;border:5px solid var(--brand-blue)}
  .cover-name{position:absolute;left:0;top:138px;width:399px;text-align:center;font-family:'Libre Baskerville',serif;font-weight:700;color:var(--ink);font-size:26px;line-height:34px;letter-spacing:3px}
  .cover-arch{position:absolute;left:24px;top:228px;width:354px;height:620px;background:var(--pale-blue);border-radius:177px 177px 0 0}
  .cover-ring{left:34px;top:241px;width:332px;height:332px}
  .care-photo{left:40px;top:247px;width:320px;height:320px;background:radial-gradient(circle at 50% 55%,#8d9bbd 0%,#4a6bb0 45%,#2e3e6a 100%)}
  .cover-title{position:absolute;left:0;top:612px;width:399px;text-align:center;font-family:'Tinos',serif;font-size:27.5px;line-height:34px;color:var(--ink)}
  .cover-rule{left:107px;top:727px;width:186px}
  .web-pill{position:absolute;left:48px;top:771px;width:304px;height:33px;border-radius:17px;background:var(--brand-blue);color:var(--white);font-size:14.6px;font-weight:300;display:flex;align-items:center;justify-content:center}
</style>
</head>
<body>
<main class="brochure">

  <section class="panel-intro">
    <div class="intro-backdrop"></div>
    <div class="photo-ring intro-ring"></div>
    <div class="photo laser-photo" role="img" aria-label="Photo of a foot resting under a cold laser treatment device glowing pink"></div>
    <div class="rule intro-rule"></div>
    <p class="intro-text">At Brightmere Foot Works, we are your experts at treating fungal nail infections and understand that fungal nail infections can reduce your confidence to wearing open toe shoes and bare feet due to thickened, yellow or irregularly shaped nails. We also understand that getting rid of a fungal nail infection can be extremely difficult involving treatments that are laborious, time consuming and usually unsuccessful.</p>
  </section>

  <section class="panel-contact">
    <div class="feet-photo" role="img" aria-label="Blue-toned photo of two bare feet standing side by side"></div>
    <div class="contact-name">Brightmere Foot Works</div>
    <div class="contact-icons">
      <span class="icon-badge"><svg viewBox="0 0 24 24"><path d="M12 2a7 7 0 0 0-7 7c0 5 7 13 7 13s7-8 7-13a7 7 0 0 0-7-7z" fill="var(--brand-blue)"/><circle cx="12" cy="9" r="2.6" fill="#fff"/></svg></span>
      <span class="icon-badge"><svg viewBox="0 0 24 24"><path d="M6.6 3.5l2.6 3.6-1.6 2.2a11 11 0 0 0 7.1 7.1l2.2-1.6 3.6 2.6-1.3 3a3 3 0 0 1-3 1.3A16 16 0 0 1 2.3 7.8a3 3 0 0 1 1.3-3z" fill="var(--brand-blue)"/></svg></span>
      <span class="icon-badge"><svg viewBox="0 0 24 24"><rect x="3" y="6" width="18" height="12" fill="none" stroke="var(--brand-blue)" stroke-width="2"/><path d="M3 6l9 7 9-7M3 18l7-6M21 18l-7-6" fill="none" stroke="var(--brand-blue)" stroke-width="1.6"/></svg></span>
      <span class="icon-badge"><svg viewBox="0 0 24 24" fill="none" stroke="var(--brand-blue)" stroke-width="1.6"><circle cx="12" cy="12" r="9"/><ellipse cx="12" cy="12" rx="4" ry="9"/><path d="M3 12h18M4.5 7.5h15M4.5 16.5h15"/></svg></span>
    </div>
    <p class="contact-line" style="top:681px">14 Larkspur Lane, Ferndale Central</p>
    <p class="contact-line" style="top:715px">(07) 555 0184</p>
    <p class="contact-line" style="top:749px">reception@brightmerefootworks.co.nz</p>
    <p class="contact-line" style="top:784px">www.brightmerefootworks.co.nz</p>
  </section>

  <section class="panel-cover">
    <div class="cover-mark"></div>
    <h1 class="cover-name">BRIGHTMERE<br>FOOT WORKS</h1>
    <div class="cover-arch"></div>
    <div class="photo-ring cover-ring"></div>
    <div class="photo care-photo" role="img" aria-label="Photo of gloved hands examining a patient's toenails"></div>
    <h2 class="cover-title">YOUR COMPLETE<br>GUIDE TO FUNGAL<br>NAIL INFECTIONS</h2>
    <div class="rule cover-rule"></div>
    <div class="web-pill">www.brightmerefootworks.co.nz</div>
  </section>

</main>
</body>
</html>
```